Florida-based Coastal Landscaping Company Needs Letterhead Designs

We are a newly established Florida-based, coastal landscaping company that is looking for some really innovative flyers that we can use to get our name our to affluent consumers that live on the coast of Florida (think on the beach) and small to medium sized businesses in the same area. We will be handing out 100s of thousands of these, so need a great design

Target Market(s)

Affluent consumers and small to medium sized businesses

Industry/Entity Type

It Company

Font styles to use
Sans Serif

Colors

Designer to choose colors to be used in the design.

Requirements
Must have
• Need to have company name, logo, individual name, phone number and contact info
Nice to have
• Florida - looking, island looking / paradise, but needs to focus on the landscaping elements
Should not have
• Regular generic lawn company letterhead designs. We are a top tier landscape design / build plus maintenance firm, so not your mom and pop lawn mowing company

```html
<!DOCTYPE html>
<html lang="en">
<head>
<meta charset="utf-8">
<title>Tidegarden Letterhead</title>
<link rel="stylesheet" href="https://fonts.googleapis.com/css2?family=Lato:wght@400;700&display=swap">
<style>
  :root {
    --teal: #1f9fc0;
    --teal-soft: #d6ecf5;
    --ink: #222a30;
    --white: #ffffff;
  }
  html, body {
    margin: 0;
    padding: 0;
    overflow: hidden;
    background: var(--white);
  }
  .letterhead {
    position: relative;
    width: 927px;
    height: 1200px;
    overflow: hidden;
    background: var(--white);
    font-family: "Lato", sans-serif;
    color: var(--ink);
  }
  .brand {
    position: absolute;
    left: 54px;
    top: 88px;
    display: flex;
    align-items: center;
    gap: 12px;
  }
  .brand-dot {
    width: 14px;
    height: 14px;
    border-radius: 50%;
    background: var(--teal);
  }
  .brand-name {
    font-size: 30px;
    font-weight: 400;
    letter-spacing: 1px;
    line-height: 1;
    color: var(--teal);
  }
  .contact-list {
    position: absolute;
    left: 630px;
    top: 56px;
    margin: 0;
    padding: 0;
    list-style: none;
  }
  .contact-list li {
    display: flex;
    align-items: center;
    height: 23px;
    font-size: 12.5px;
    white-space: nowrap;
  }
  .contact-list svg {
    width: 14px;
    height: 14px;
    margin-right: 10px;
    fill: var(--teal);
    flex: none;
  }
  .header-rule {
    position: absolute;
    left: 0;
    top: 159px;
    width: 927px;
    height: 6px;
    background: var(--teal);
  }
  .wave-area {
    position: absolute;
    left: 68px;
    top: 830px;
    width: 774px;
    height: 268px;
    background: radial-gradient(ellipse at center, var(--teal-soft) 0%, rgba(214, 236, 245, 0.5) 45%, rgba(255, 255, 255, 0) 72%);
  }
  .footer-band {
    position: absolute;
    left: 0;
    top: 1156px;
    width: 927px;
    height: 44px;
    background: var(--teal);
    display: flex;
    justify-content: center;
    align-items: center;
    gap: 14px;
    color: var(--white);
    font-size: 12.5px;
    white-space: nowrap;
  }
  .footer-item {
    display: flex;
    align-items: center;
    gap: 8px;
  }
  .footer-item svg {
    width: 14px;
    height: 14px;
    fill: var(--white);
  }
</style>
</head>
<body>
<main class="letterhead">
  <header>
    <div class="brand">
      <span class="brand-dot"></span>
      <span class="brand-name">TIDEGARDEN</span>
    </div>
    <ul class="contact-list">
      <li><svg viewBox="0 0 24 24"><path d="M6.6 10.8a15.1 15.1 0 0 0 6.6 6.6l2.2-2.2c.3-.3.7-.4 1-.2 1.1.4 2.3.6 3.6.6.6 0 1 .4 1 1V20c0 .6-.4 1-1 1A17 17 0 0 1 3 4c0-.6.4-1 1-1h3.5c.6 0 1 .4 1 1 0 1.3.2 2.5.6 3.6.1.3 0 .7-.2 1z"/></svg>+1 305 555 0142</li>
      <li><svg viewBox="0 0 24 24"><path d="M2 5h20v14H2zm2 2v.5l8 5 8-5V7zm0 2.8V17h16V9.8l-8 5z"/></svg>hello@tidegarden.com</li>
      <li><svg viewBox="0 0 24 24"><path d="M12 2a10 10 0 1 0 0 20 10 10 0 0 0 0-20zm6.9 6h-2.9a15 15 0 0 0-1.3-3.6A8 8 0 0 1 18.9 8zM12 4c.8 1.2 1.5 2.5 1.9 4h-3.8c.4-1.5 1.1-2.8 1.9-4zM4.3 14a8 8 0 0 1 0-4h3.4a16 16 0 0 0 0 4zm.8 2h2.9c.3 1.3.8 2.5 1.3 3.6A8 8 0 0 1 5.1 16zM8 8H5.1a8 8 0 0 1 4.2-3.6C8.8 5.5 8.3 6.7 8 8zm4 12c-.8-1.2-1.5-2.5-1.9-4h3.8c-.4 1.5-1.1 2.8-1.9 4zm2.3-6H9.7a14 14 0 0 1 0-4h4.6a14 14 0 0 1 0 4zm.4 5.6c.5-1.1 1-2.3 1.3-3.6h2.9a8 8 0 0 1-4.2 3.6zm1.6-5.6a16 16 0 0 0 0-4h3.4a8 8 0 0 1 0 4z"/></svg>tidegarden.com</li>
      <li><svg viewBox="0 0 24 24"><path d="M12 2a7 7 0 0 0-7 7c0 5.2 7 13 7 13s7-7.8 7-13a7 7 0 0 0-7-7zm0 9.5A2.5 2.5 0 1 1 12 6.5a2.5 2.5 0 0 1 0 5z"/></svg>Suite 12, 400 Ocean Dr FL 33139</li>
    </ul>
    <div class="header-rule"></div>
  </header>

  <div class="wave-area" role="img" aria-label="Soft decorative wave ornament in pale blue and grey"></div>

  <footer class="footer-band">
    <span class="footer-item"><svg viewBox="0 0 24 24"><path d="M12 2a10 10 0 1 0 0 20 10 10 0 0 0 0-20zm6.9 6h-2.9a15 15 0 0 0-1.3-3.6A8 8 0 0 1 18.9 8zM12 4c.8 1.2 1.5 2.5 1.9 4h-3.8c.4-1.5 1.1-2.8 1.9-4zM4.3 14a8 8 0 0 1 0-4h3.4a16 16 0 0 0 0 4zm.8 2h2.9c.3 1.3.8 2.5 1.3 3.6A8 8 0 0 1 5.1 16zM8 8H5.1a8 8 0 0 1 4.2-3.6C8.8 5.5 8.3 6.7 8 8zm4 12c-.8-1.2-1.5-2.5-1.9-4h3.8c-.4 1.5-1.1 2.8-1.9 4zm2.3-6H9.7a14 14 0 0 1 0-4h4.6a14 14 0 0 1 0 4zm.4 5.6c.5-1.1 1-2.3 1.3-3.6h2.9a8 8 0 0 1-4.2 3.6zm1.6-5.6a16 16 0 0 0 0-4h3.4a8 8 0 0 1 0 4z"/></svg>www.tidegarden.com</span>
    <span class="footer-item"><svg viewBox="0 0 24 24"><path d="M12 2a7 7 0 0 0-7 7c0 5.2 7 13 7 13s7-7.8 7-13a7 7 0 0 0-7-7zm0 9.5A2.5 2.5 0 1 1 12 6.5a2.5 2.5 0 0 1 0 5z"/></svg>Suite 12, 400 Ocean Dr FL 33139</span>
  </footer>
</main>
</body>
</html>
```